Norvel Composites Brochure Design

Looking to create a Brochure to outline the products and services that we provide. The business manufactures and supplies fibreglass resins and materials within Australia. Looking for a modern easy to ready brochure that covers the products that we sell, and outlines our business goals of excellent customer service, able to handle any project large or small.
Our website is www.norvelcomposites.com.au.
Not 100% sure on the design, interested in seeing different design options and ideas.

Target Market(s)

Fibreglass and Composite manufacturers
Boat Buliders
Fibreglass Swimming Pool Manufacturers
Resin Art, Casting
Carbon Fibre Composites
Tank Manufacturers
Surfboard design and repairs

Industry/Entity Type

Business

Font styles to use
Sans Serif

Colors

Designer to choose colors to be used in the design.

Requirements
Must have
• Modern Design, easy to read

```html
<!DOCTYPE html>
<html lang="en">
<head>
<meta charset="utf-8">
<title>Norvel Composites Brochure Spread</title>
<link href="https://fonts.googleapis.com/css2?family=Encode+Sans+Condensed:wght@400;500;600;700&display=swap" rel="stylesheet">
<style>
  :root{
    --bg:#d9d9da;
    --page:#ffffff;
    --row-alt:#e6e6e7;
    --row:#f6f6f6;
    --ink:#2b2b33;
    --label:#33333a;
    --hero-a:#3d3c7a;
    --hero-b:#6b6fb2;
    --hero-c:#2b2b5c;
    --red:#e6232f;
    --red-light:#f26b75;
    --white:#ffffff;
  }
  *{box-sizing:border-box;margin:0;padding:0}
  html,body{width:1200px;height:1200px;overflow:hidden}
  body{background:var(--bg);font-family:"Encode Sans Condensed",sans-serif;color:var(--ink);position:relative}
  .spread{position:absolute;left:30px;top:195px;width:1140px;height:810px;display:flex;box-shadow:0 10px 30px rgba(0,0,0,.2)}
  .page{width:570px;height:100%;background:var(--page);display:flex;flex-direction:column}
  .hero{height:280px;position:relative;background:linear-gradient(160deg,var(--hero-b),var(--hero-a) 55%,var(--hero-c))}
  .band{height:16px;background:linear-gradient(90deg,var(--red-light),var(--red))}
  .page--right .band{background:linear-gradient(90deg,var(--red),var(--red-light) 60%,var(--red))}
  .hero-title{position:absolute;left:125px;top:132px;color:var(--white);font-weight:600;font-size:21px;letter-spacing:.2px}
  .reasons{flex:1;display:flex;flex-direction:column}
  .reason{flex:1;display:flex;align-items:center;gap:30px;padding:0 40px 0 20px;background:var(--row)}
  .reason:nth-child(odd){background:var(--row-alt)}
  .reason-icon{width:78px;height:62px;flex:none;border-radius:6px}
  .reason p{font-size:14.5px;line-height:1.35;color:var(--ink)}
  .cert-badge{width:78px;height:40px;flex:none;border:2px solid var(--ink);border-radius:20px;display:flex;align-items:center;padding-left:4px}
  .cert-badge span{width:30px;height:30px;border-radius:50%;border:2px solid var(--ink)}
  .partners-box{position:absolute;left:14px;top:22px;right:14px;bottom:22px;border:1.5px solid var(--white);padding:20px 20px;color:var(--white)}
  .partners-box h2{font-size:21px;font-weight:600;margin-bottom:14px}
  .partners-box p{font-size:13.6px;line-height:1.32;margin-bottom:12px}
  .partners-box strong{font-weight:700}
  .products{flex:1;display:grid;grid-template-columns:repeat(4,1fr);grid-template-rows:repeat(5,1fr);padding:12px 30px 14px}
  .product{display:flex;flex-direction:column;align-items:center;justify-content:center;gap:6px}
  .product-photo{width:66px;height:62px;border-radius:2px}
  .product span{font-size:10.5px;text-transform:uppercase;color:var(--label);text-align:center;line-height:1.2;max-width:90px}
</style>
</head>
<body>
<div class="spread">
  <section class="page page--left">
    <div class="hero" role="img" aria-label="Aerial photograph of a city skyline in blue-purple duotone">
      <h1 class="hero-title">WHY CHOOSE NORVEL COMPOSITES?</h1>
    </div>
    <div class="band"></div>
    <div class="reasons">
      <div class="reason">
        <div class="reason-icon" role="img" aria-label="Factory illustration" style="background:linear-gradient(#8fd0d6,#3fb6bd)"></div>
        <p>Norvel Composites has been supplying composite products all over Australia for over 16 years.</p>
      </div>
      <div class="reason">
        <div class="reason-icon" role="img" aria-label="Globe illustration" style="background:radial-gradient(circle,#6fa0e0,#2f63b8 70%,transparent 72%)"></div>
        <p>With an extensive purchasing network all over the world. We import and sell the top composites brands on the market.</p>
      </div>
      <div class="reason">
        <div class="cert-badge" role="img" aria-label="Quality certification badge"><span></span></div>
        <p>We use a current ISO 9001 Quality Management System. Our operations and processes are to the highest industry standard.</p>
      </div>
      <div class="reason">
        <div class="reason-icon" role="img" aria-label="Laptop with parcels illustration" style="background:linear-gradient(135deg,#c9c9cc,#8a7a66)"></div>
        <p>Our online trade centre is the largest most extensive composite store in Australia. Our site is equipped with the latest Secure Socket Layer SSL Encryption to protect your security and online details</p>
      </div>
      <div class="reason">
        <div class="reason-icon" role="img" aria-label="Rising bar chart illustration" style="background:linear-gradient(135deg,#f1d27a,#d8262c)"></div>
        <p>Fully equipped and dedicated laboratory for product testing, evaluation and development. We continually look to improve our products and services everyday.</p>
      </div>
      <div class="reason">
        <div class="reason-icon" role="img" aria-label="Customer network illustration" style="background:linear-gradient(135deg,#d8d8da,#e0553d)"></div>
        <p>We pride ourselves on customer service. We strive to provide a personalised service to each and everyone of our customers.</p>
      </div>
    </div>
  </section>
  <section class="page page--right">
    <div class="hero" role="img" aria-label="Aerial photograph of city towers and waterway in blue-purple duotone">
      <div class="partners-box">
        <h2>SUPPLY PARTNERS</h2>
        <p>We value our partnerships with our many suppliers. We work hard to establish and maintain these partnerships to bring you the best composite materials in the industry</p>
        <p><strong>Norvel Composites</strong> has an impressive list of supply partners and we have a very large purchasing network all over the world. For many years we have developed business relationships with some of the world's top chemical and composites manufacturers. So you can be assured that you are getting the highest quality materials available. We are proud to be in partnerships with world leaders such as <strong>Halvard Chemicals</strong>, <strong>Meridian Initiators</strong>, <strong>Releaso</strong> and <strong>Fortex Glass</strong>.</p>
      </div>
    </div>
    <div class="band"></div>
    <div class="products">
      <div class="product"><div class="product-photo" role="img" aria-label="Abrasive roll photo" style="background:#e4b04e"></div><span>Kestrel Abrasives</span></div>
      <div class="product"><div class="product-photo" role="img" aria-label="Compound tin photo" style="background:linear-gradient(#dcdcdc,#555)"></div><span>Kestrel Compounds</span></div>
      <div class="product"><div class="product-photo" role="img" aria-label="Casting resin containers photo" style="background:linear-gradient(#eef,#9aa)"></div><span>Casting &amp; Art</span></div>
      <div class="product"><div class="product-photo" role="img" aria-label="Catalyst bottle photo" style="background:linear-gradient(#f4f4f4,#cfd8df)"></div><span>Catalyst</span></div>
      <div class="product"><div class="product-photo" role="img" aria-label="Cleaning chemical drums photo" style="background:linear-gradient(#f5c6d4,#8bc58a)"></div><span>Cleaning Chemicals</span></div>
      <div class="product"><div class="product-photo" role="img" aria-label="Core material sheet photo" style="background:linear-gradient(135deg,#d8d6f0,#f4f4fa)"></div><span>Core Materials</span></div>
      <div class="product"><div class="product-photo" role="img" aria-label="Epoxy containers photo" style="background:linear-gradient(#f2f2f2,#b9c6d2)"></div><span>Epoxy Systems</span></div>
      <div class="product"><div class="product-photo" role="img" aria-label="Respirator mask photo" style="background:radial-gradient(#555,#bbb)"></div><span>Equipment &amp;<br>Add-ons</span></div>
      <div class="product"><div class="product-photo" role="img" aria-label="Filler powder photo" style="background:radial-gradient(#eee,#333)"></div><span>Fillers</span></div>
      <div class="product"><div class="product-photo" role="img" aria-label="Finish coat pails photo" style="background:linear-gradient(#f2f2f2,#7e8aa3)"></div><span>Finish Coat</span></div>
      <div class="product"><div class="product-photo" role="img" aria-label="Gelcoat pails photo" style="background:linear-gradient(#eee,#5f6b86)"></div><span>Gelcoat</span></div>
      <div class="product"><div class="product-photo" role="img" aria-label="Mould release tins photo" style="background:linear-gradient(#444,#c9b7c2)"></div><span>Mould Release</span></div>
      <div class="product"><div class="product-photo" role="img" aria-label="Solvent tins photo" style="background:linear-gradient(#7a8aa6,#c94a4a)"></div><span>Solvents &amp;<br>Additives</span></div>
      <div class="product"><div class="product-photo" role="img" aria-label="Insulation board photo" style="background:linear-gradient(135deg,#bdbdbd,#e6e6e6)"></div><span>Thermoquill</span></div>
      <div class="product"><div class="product-photo" role="img" aria-label="Infusion tubing photo" style="background:linear-gradient(135deg,#fafafa,#dcdcdc)"></div><span>Vacum &amp; Infusion</span></div>
      <div class="product"><div class="product-photo" role="img" aria-label="Vinylester pail photo" style="background:linear-gradient(#f6f6f6,#c8d2dc)"></div><span>Vinylester</span></div>
      <div class="product"><div class="product-photo" role="img" aria-label="Pigment jar photo" style="background:linear-gradient(#3a8a4a,#d8291f)"></div><span>Pigments</span></div>
      <div class="product"><div class="product-photo" role="img" aria-label="Polyester pail photo" style="background:linear-gradient(#f6f6f6,#c7cdd6)"></div><span>Polyster</span></div>
      <div class="product"><div class="product-photo" role="img" aria-label="Polyurethane tins photo" style="background:linear-gradient(#5a6a8a,#9aa6c0)"></div><span>Polyurethane</span></div>
      <div class="product"><div class="product-photo" role="img" aria-label="Glass fibre roll photo" style="background:linear-gradient(135deg,#e6e8ee,#b8c0cc)"></div><span>Reinforcements</span></div>
    </div>
  </section>
</div>
</body>
</html>
```